Letterhead - Quarrington Law Group

I receive a fantastic logo from you guys and I'd like to incorporate it into business cards and letterhead. I accidentally approved design No. 32361474 and contacted designer Ravindra, and Ravindra sent me the zip folder for Design No. 32361417, which I very much appreciate.
I'd like to order business cards and letterhead with Design No. 32361417 as soon as possible, but I want to make sure that you incorporate the correct design (attached). I'd also like to provide my information to add (address, phone number, email, fax) but I'm not quite sure how to do it.
The information that I would like on the business cards and letterhead is as follows:
Quarrington Law Group
Theodore K. Quarrington, Esq.
2741 Hollis Avenue, Suite 520
San Francisco, CA 94087
Office: (415) 378-6130
Fax: (415) 746-0183
ted@quarringtonlawgroup-example.com
Thanks in advance for any guidance.
Ted Quarrington
Quarrington Law Group
(415) 831-4497 (cell)

```html
<!DOCTYPE html>
<html lang="en">
<head>
<meta charset="utf-8">
<title>Quarrington Law Group – Stationery</title>
<link rel="stylesheet" href="https://fonts.googleapis.com/css2?family=Cormorant+Garamond:wght@500&family=Open+Sans:wght@400;600;700&display=swap">
<style>
  :root {
    --stage: #3b3b3d;
    --ink: #181716;
    --blue: #0b78b1;
    --grey-light: #dcdcdc;
    --grey-mid: #bdbdbd;
    --grey-dark: #3a3a3a;
    --paper: #dedede;
    --text: #222;
    --white: #f4f4f4;
  }
  * { box-sizing: border-box; margin: 0; padding: 0; }
  html, body { width: 1200px; height: 800px; overflow: hidden; }
  body { background: var(--stage); font-family: "Open Sans", Arial, sans-serif; position: relative; }

  .brand-name {
    font-family: "Cormorant Garamond", Georgia, serif;
    font-weight: 500;
    color: var(--white);
    letter-spacing: .04em;
    line-height: 1.05;
    text-transform: uppercase;
  }

  .icon { width: 14px; height: 14px; background: var(--blue); display: inline-flex; align-items: center; justify-content: center; flex: none; }
  .icon svg { width: 9px; height: 9px; fill: none; stroke: #fff; stroke-width: 1.6; stroke-linecap: round; stroke-linejoin: round; }

  /* Business cards */
  .card { position: absolute; left: 110px; width: 340px; height: 196px; background: var(--ink); overflow: hidden; }
  .card--contact { top: 100px; }
  .card--brand { top: 360px; display: flex; align-items: center; justify-content: center; }
  .card__name { position: absolute; left: 18px; top: 16px; color: var(--blue); font-size: 9.5px; font-weight: 700; text-transform: uppercase; letter-spacing: .02em; }
  .card__role { position: absolute; left: 18px; top: 31px; color: #cfcfcf; font-size: 8.5px; }
  .card__brand { position: absolute; right: 16px; top: 14px; font-size: 11px; text-align: right; }
  .card__contacts { position: absolute; left: 18px; top: 70px; width: 310px; display: grid; grid-template-columns: 160px 150px; row-gap: 9px; }
  .card__row { display: flex; align-items: center; gap: 6px; color: #d8d8d8; font-size: 7px; line-height: 1.2; white-space: nowrap; }
  .card__row .icon { width: 12px; height: 12px; }
  .card__band { position: absolute; left: 0; bottom: 0; width: 340px; height: 50px; }
  .card--brand .brand-name { font-size: 26px; text-align: center; }

  /* Letterhead */
  .letterhead { position: absolute; left: 585px; top: 40px; width: 510px; height: 720px; background: var(--paper); overflow: hidden; }
  .letterhead__header { position: absolute; left: 0; top: 0; width: 510px; height: 172px; }
  .letterhead__brand { position: absolute; left: 14px; top: 76px; font-size: 15px; width: 120px; }
  .letterhead__contacts { position: absolute; right: 14px; top: 36px; display: flex; flex-direction: column; gap: 9px; align-items: flex-end; }
  .letterhead__contacts .card__row { color: #333; font-size: 7px; gap: 6px; }
  .letterhead__contacts .icon { width: 16px; height: 16px; }
  .letterhead__contacts .address { text-align: right; line-height: 1.3; }
  .letterhead__body { position: absolute; left: 13px; right: 9px; top: 193px; color: var(--text); font-size: 8px; line-height: 14px; text-align: justify; }
  .letterhead__salutation { font-weight: 700; font-size: 8px; margin-bottom: 12px; }
  .letterhead__body p { margin-bottom: 14px; }
  .letterhead__signature { position: absolute; right: 26px; top: 610px; width: 110px; border-top: 1px solid #222; padding-top: 4px; text-align: center; font-size: 7.5px; font-style: italic; color: #222; }
  .letterhead__footer { position: absolute; left: 0; bottom: 0; width: 510px; height: 66px; }
</style>
</head>
<body>

<svg width="0" height="0" style="position:absolute" aria-hidden="true">
  <symbol id="i-phone" viewBox="0 0 10 10"><rect x="3" y="1" width="4" height="8" rx="1"/></symbol>
  <symbol id="i-fax" viewBox="0 0 10 10"><rect x="1.5" y="4" width="7" height="4"/><path d="M3 4V1.5h4V4M3 8v1h4V8"/></symbol>
  <symbol id="i-mail" viewBox="0 0 10 10"><rect x="1" y="2.5" width="8" height="5.5"/><path d="M1 2.5l4 3 4-3"/></symbol>
  <symbol id="i-web" viewBox="0 0 10 10"><circle cx="5" cy="5" r="4"/><path d="M1 5h8M5 1c2 2.4 2 5.6 0 8M5 1c-2 2.4-2 5.6 0 8"/></symbol>
  <symbol id="i-pin" viewBox="0 0 10 10"><path d="M5 9.2S2 6 2 4a3 3 0 016 0c0 2-3 5.2-3 5.2z"/><circle cx="5" cy="4" r="1"/></symbol>
</svg>

<!-- Business card: contact side -->
<section class="card card--contact">
  <div class="card__name">Theodore K. Quarrington, Esq.</div>
  <div class="card__role">Lawyer</div>
  <div class="brand-name card__brand">Quarrington<br>Law Group</div>
  <div class="card__contacts">
    <div class="card__row"><span class="icon"><svg><use href="#i-phone"/></svg></span>(415) 831-4497</div>
    <div class="card__row"><span class="icon"><svg><use href="#i-fax"/></svg></span>(415) 746-0183</div>
    <div class="card__row"><span class="icon"><svg><use href="#i-phone"/></svg></span>(415) 378-6130</div>
    <div class="card__row"><span class="icon"><svg><use href="#i-mail"/></svg></span>ted@quarringtonlawgroup-example.com</div>
    <div class="card__row"><span class="icon"><svg><use href="#i-web"/></svg></span>www.quarringtonlawgroup-example.com</div>
    <div class="card__row"><span class="icon"><svg><use href="#i-pin"/></svg></span><span>2741 Hollis Avenue, Suite 520<br>San Francisco, CA 94087</span></div>
  </div>
  <svg class="card__band" viewBox="0 0 340 50" preserveAspectRatio="none" aria-hidden="true">
    <polygon points="0,14 60,14 90,50 0,50" fill="var(--grey-light)"/>
    <polygon points="60,14 300,14 285,30 75,30" fill="var(--blue)"/>
    <polygon points="75,30 285,30 270,50 90,50" fill="#0f0f0f"/>
    <polygon points="300,14 340,14 340,50 270,50" fill="var(--grey-light)"/>
  </svg>
</section>

<!-- Business card: brand side -->
<section class="card card--brand">
  <div class="brand-name">Quarrington<br>Law Group</div>
</section>

<!-- Letterhead -->
<article class="letterhead">
  <svg class="letterhead__header" viewBox="0 0 510 172" preserveAspectRatio="none" aria-hidden="true">
    <rect width="510" height="172" fill="var(--grey-light)"/>
    <polygon points="290,0 510,0 510,172 370,172" fill="var(--grey-mid)" opacity=".45"/>
    <polygon points="240,0 262,0 251,36" fill="var(--grey-mid)"/>
    <polygon points="0,0 135,0 245,172 0,172" fill="var(--ink)"/>
    <polygon points="140,40 270,40 318,133 205,133" fill="var(--blue)"/>
    <polygon points="205,133 245,133 220,172 195,172" fill="var(--grey-dark)"/>
  </svg>
  <div class="brand-name letterhead__brand">Quarrington<br>Law Group</div>
  <div class="letterhead__contacts">
    <div class="card__row">(415) 378-6130<span class="icon"><svg><use href="#i-phone"/></svg></span></div>
    <div class="card__row">(415) 746-0183<span class="icon"><svg><use href="#i-fax"/></svg></span></div>
    <div class="card__row">ted@quarringtonlawgroup-example.com<span class="icon"><svg><use href="#i-mail"/></svg></span></div>
    <div class="card__row">www.quarringtonlawgroup-example.com<span class="icon"><svg><use href="#i-web"/></svg></span></div>
    <div class="card__row"><span class="address">2741 Hollis Avenue, Suite 520<br>San Francisco, CA 94087</span><span class="icon"><svg><use href="#i-pin"/></svg></span></div>
  </div>

  <div class="letterhead__body">
    <div class="letterhead__salutation">DEAR SIR,</div>
    <p>Lorem Ipsum is simply dummy text of the printing and typesetting industry. Lorem Ipsum has been the industry's standard dummy text ever since the 1500s, when an unknown printer took a galley of type and scrambled it to make a type specimen book. It has survived not only five centuries, but also the leap into electronic typesetting, remaining essentially unchanged.</p>
    <p>It was popularised in the 1960s with the release of Letraset sheets containing Lorem Ipsum passages, and more recently with desktop publishing software like Aldus PageMaker including versions of Lorem Ipsum.</p>
    <p>It is a long established fact that a reader will be distracted by the readable content of a page when looking at its layout. The point of using Lorem Ipsum is that it has a more or less normal distribution of letters, as opposed to using 'Content here, content here', making it look like readable English. Many desktop publishing packages and web page editors now use Lorem Ipsum as their default model text, and a search for 'lorem ipsum' will uncover many web sites still in their infancy. If you are going to use a passage of Lorem Ipsum, you need to be sure there isn't anything embarrassing hidden in the middle of text.</p>
  </div>

  <div class="letterhead__signature">SIGNATURE</div>

  <svg class="letterhead__footer" viewBox="0 0 510 66" preserveAspectRatio="none" aria-hidden="true">
    <polygon points="0,0 62,0 112,66 0,66" fill="var(--grey-mid)"/>
    <polygon points="72,26 428,26 448,52 92,52" fill="var(--blue)"/>
    <polygon points="404,0 510,0 510,66 468,66" fill="var(--ink)"/>
    <polygon points="404,0 420,0 412,26 392,26" fill="var(--grey-dark)"/>
  </svg>
</article>

</body>
</html>
```